Rusty Clem's BBQ is an online seasoning and other food sales business.

I need a website and store to launch this new business. The site must be compatible to smart phones. Most of the marketing will be done through short comedic social media videos that are unrelated to cooking for entertainment purposes. I will also have cooking instructional videos. I will sell merchandise in the future. Products for sale now will be my Beef Rub and Pork Rub. In 2 months I will have an All Seasoning and Cajun Seasoning. Later this year I will add Rusty Clem's Ranch Beans and a BBQ sauce along with merchandise. I have a logo and labels designs for the seasonings. I will upload pictures of the bottles soon. I do not want this to look like a generic BBQ website because my products are not inclusive to smoking meat. No pigs or cartoon pictures on my website besides my logo. Stock photos of brisket, pork butt, ribs and chicken are welcome. The company is fun and entertaining unlike any seasoning in this world. We will make you laugh and happy through our products and videos. I had to use Rusty Clem's BBQ name due to trademark issue. Rusty Clem's is already trademarked. I'm trademarking Rusty Clem's BBQ. I'm not a huge fan of the BBQ part because it may deter some people from buying the product thinking it only for smoking meat. The roots of my company came from smoking delicious meets as a hobby and small catering jobs. I want people to use this on everything from eggs to soups, stews, vegetables, pastas, beans and many more side dishes. If you eat meat prepared in any way, these seasonings are for you. I'm more than happy to get you other pictures of meat and add content as required. I'm just setting up this company and will get you the required information upon request. I attached a sample of a blue and green label for the All Seasoning which is not finalized yet. I will use the blue label version with updated nutrient facts and ingredients.

```html
<!DOCTYPE html>
<html lang="en">
<head>
<meta charset="utf-8">
<title>Rusty Clem's BBQ — Seasoning for Everything</title>
<link rel="stylesheet" href="https://fonts.googleapis.com/css2?family=Roboto+Condensed:wght@700&family=Arimo:wght@400;700&family=Open+Sans:wght@600&display=swap">
<style>
  :root{
    --cream:#f4ebd9;
    --red:#bb1d24;
    --red-deep:#a3181e;
    --green:#2f5f3a;
    --green-soft:#5d8a5c;
    --yellow:#fbe134;
    --ink:#1a1513;
    --white:#ffffff;
    --tag-green:#4a6d3a;
    --tag-line:#b8b64a;
    --para-light:#e6dcc6;
  }
  *{box-sizing:border-box;margin:0;padding:0}
  html,body{width:1200px;height:2248px;overflow:hidden}
  body{background:var(--cream);font-family:"Arimo",Arial,sans-serif;color:var(--ink);position:relative}
  .cond{font-family:"Roboto Condensed","Arial Narrow",sans-serif;font-weight:700;text-transform:uppercase}
  .abs{position:absolute}

  /* header */
  .site-header{position:absolute;left:0;top:0;width:1200px;height:66px;background:var(--cream);border-bottom:2px solid var(--ink)}
  .brand{position:absolute;left:48px;top:11px;display:flex;align-items:center;gap:10px}
  .brand-mark{width:46px;height:46px;border-radius:50%;background:var(--red)}
  .brand-name{font-family:"Roboto Condensed",sans-serif;font-weight:700;font-size:15px;text-transform:uppercase}
  .nav{position:absolute;right:46px;top:17px;display:flex;align-items:center;gap:13px}
  .nav a{font-family:"Roboto Condensed",sans-serif;font-weight:700;font-size:9.5px;text-transform:uppercase;color:var(--ink);text-decoration:none}

  .btn{display:inline-flex;align-items:center;justify-content:center;font-family:"Roboto Condensed",sans-serif;font-weight:700;text-transform:uppercase;font-size:11px;border:2px solid var(--ink);box-shadow:4px 4px 0 var(--yellow);text-decoration:none;color:var(--white);background:var(--red)}
  .btn--yellow{background:var(--yellow);color:var(--ink);box-shadow:4px 4px 0 var(--red)}
  .nav .btn{width:100px;height:34px;color:var(--white);margin-left:1px}

  /* hero */
  .hero{position:absolute;left:0;top:66px;width:1200px;height:628px;overflow:hidden}
  .hero svg{position:absolute;left:0;top:0}
  .badge{left:60px;top:163px;height:25px;padding:0 9px;background:var(--yellow);border:2px solid var(--ink);font-size:11px;display:flex;align-items:center}
  .hero-title{left:60px;top:200px;font-size:76px;line-height:66px;color:var(--white);text-shadow:4px 4px 0 var(--ink)}
  .hero-copy{left:60px;top:351px;width:500px;font-size:14.5px;line-height:21.5px;font-weight:700;color:var(--white)}
  .hero-actions{left:60px;top:435px;display:flex;gap:12px}
  .hero-actions .btn{height:33px;padding:0 15px}
  .product-frame{left:783px;top:129px;width:356px;height:371px;border:2px solid var(--yellow)}
  .product-card{left:800px;top:140px;width:324px;height:350px;background:var(--white);box-shadow:8px 0 0 rgba(60,20,20,.45)}
  .product-label{left:823px;top:151px;width:280px;height:332px;background:linear-gradient(180deg,#8c9a5a 0%,#8c9a5a 52%,#211d1b 52%,#211d1b 100%)}

  /* collection */
  .eyebrow{font-family:"Roboto Condensed",sans-serif;font-weight:700;font-size:10px;text-transform:uppercase;color:var(--red)}
  .section-title{font-size:65px;line-height:58.5px}
  .cards{left:60px;top:1164px;display:flex;gap:13px}
  .card{position:relative;width:260px;height:196px;background:var(--white);border:2px solid var(--ink);padding:16px 17px}
  .card h3{font-family:"Roboto Condensed",sans-serif;font-weight:700;font-size:23px;text-transform:uppercase;color:var(--red);line-height:26px}
  .card p{margin-top:6px;font-size:11.5px;line-height:15px;color:#3a3330}
  .card .btn{position:absolute;left:17px;bottom:15px;width:224px;height:33px}

  /* positioning */
  .positioning{position:absolute;left:0;top:1388px;width:1200px;height:349px;background:var(--green)}
  .pos-copy{left:579px;top:90px;width:560px;font-family:"Open Sans",sans-serif;font-weight:600;font-size:14.5px;line-height:20px;color:var(--para-light)}
  .tags{left:579px;top:193px;display:flex;gap:11px}
  .tag{width:180px;height:41px;border:2px solid var(--tag-line);background:var(--tag-green);color:var(--white);font-family:"Roboto Condensed",sans-serif;font-weight:700;font-size:11px;text-transform:uppercase;display:flex;align-items:center;padding-left:13px}

  /* content engine */
  .content{position:absolute;left:0;top:1737px;width:1200px;height:511px;background:var(--ink)}
  .video-slot{left:60px;top:111px;width:512px;height:288px;border:2px solid var(--yellow);background:linear-gradient(135deg,#9b1b24 0%,#553259 50%,#16558f 100%);text-align:center;padding-top:23px;color:var(--white);font-size:52px;line-height:62px}
  .content-copy{left:627px;top:356px;width:500px;font-size:13px;line-height:20px;color:var(--white)}
</style>
</head>
<body>

<header class="site-header">
  <div class="brand"><span class="brand-mark"></span><span class="brand-name">Rusty Clem's BBQ</span></div>
  <nav class="nav">
    <a href="#">Shop Rubs</a><a href="#">Our Story</a><a href="#">Videos</a>
    <a class="btn" href="#">Buy Seasoning</a>
  </nav>
</header>

<section class="hero">
  <svg width="1200" height="628" viewBox="0 0 1200 628" role="img" aria-label="Bold green and red background with a repeating circle pattern">
    <rect width="1200" height="628" fill="#bf242c"/>
    <polygon points="0,0 690,0 70,628 0,628" fill="var(--green-soft)"/>
  </svg>
  <div class="abs badge cond">Veteran Owned Seasoning</div>
  <h1 class="abs hero-title cond">Not just for<br>BBQ.</h1>
  <p class="abs hero-copy">Rusty Clem's BBQ launches with bold Beef Rub and Pork Rub, then expands into all seasoning, Cajun seasoning, beans, sauce, merch, and entertaining cooking content.</p>
  <div class="abs hero-actions">
    <a class="btn" href="#">Shop the Rubs</a>
    <a class="btn btn--yellow" href="#">Watch Recipes</a>
  </div>
  <div class="abs product-frame"></div>
  <div class="abs product-card"></div>
  <div class="abs product-label" role="img" aria-label="Beef Rub seasoning package label"></div>
</section>

<section>
  <p class="abs eyebrow" style="left:60px;top:768px">Launch Collection</p>
  <h2 class="abs section-title cond" style="left:60px;top:787px">Seasoning for meat,<br>eggs, soups,<br>vegetables, pasta,<br>beans, and<br>everything in<br>between.</h2>
  <div class="abs cards">
    <article class="card"><h3>Beef Rub</h3><p>Built for steaks, roasts, burgers, brisket, and big flavor.</p><a class="btn" href="#">Add to Cart</a></article>
    <article class="card"><h3>Pork Rub</h3><p>Sweet and savory for ribs, shoulders, chicken, and everyday cooking.</p><a class="btn" href="#">Add to Cart</a></article>
    <article class="card"><h3>All Seasoning</h3><p>The flexible blue-label hero for meat and other foods.</p><a class="btn" href="#">Coming Soon</a></article>
    <article class="card"><h3>Cajun Seasoning</h3><p>A future drop for heat, depth, and easy weeknight meals.</p><a class="btn" href="#">Notify Me</a></article>
  </div>
</section>

<section class="positioning">
  <p class="abs eyebrow" style="left:60px;top:77px">Brand Positioning</p>
  <h2 class="abs section-title cond" style="left:60px;top:97px;color:var(--white)">Funny on<br>video. Serious<br>about flavor.</h2>
  <p class="abs pos-copy">Lorem ipsum dolor sit amet, consectetur adipiscing elit, sed do eiusmod tempor incididunt ut labore et dolore magna aliqua. Ut enim ad minim veniam, quis nostrud exercitation ullamco laboris nisi ut aliquip ex ea commodo consequat. non proident, sunt in culpa qui officia deserunt mollit anim id est laborum</p>
  <div class="abs tags">
    <span class="tag">No Pig Visuals</span><span class="tag">Mobile-First Store</span><span class="tag">Product-Led Conversion</span>
  </div>
</section>

<section class="content">
  <div class="abs video-slot cond" role="img" aria-label="Short video player area">Short videos live<br>here</div>
  <p class="abs eyebrow" style="left:627px;top:79px">Content Engine</p>
  <h2 class="abs section-title cond" style="left:627px;top:98px;color:var(--white)">Social clips<br>become the<br>store’s<br>personality.</h2>
  <p class="abs content-copy">The site leaves room for comedic social videos, cooking instructions, and future merch without letting entertainment overpower the product path.</p>
  <a class="abs btn" href="#" style="left:629px;top:401px;height:33px;padding:0 13px">Watch Recipes</a>
</section>

</body>
</html>
```